Fun but professional website required for school teaching consultancy.

Dear Designers,

I have an interesting brief for you. My client is a skilled teacher who is looking to promote her consultancy that provides bespoke training and support to other teachers.

She would like a website that promotes her philosophy for working with children, which is essentially that she wants to create a fun and creative learning environment for them, whilst maintaining the professionalism that is also required to succeed. Representation of the balance between these two points is crucial to the design.

Typically these kind of websites are pretty boring so we need something fun and vibrant, not uninviting ie those typical images of a teacher sat behind a desk or anything overly formal.

Here is an example of what we do not want: http://www.brightmarrowlearning.co.uk/ - in this one although my client liked the layout, she hated the graphics.

Here is a website that she really liked and captured the vibe of what she is trying to promote about herself: http://www.pellowfieldkidsplace.com/ - this design indicates fun with learning, happy kids, lively colours and still has a professional feel as well.

If you have any further questions, please ask

Many thanks,

Garth

PS Enclosed please find a whole bunch of resources (including site map) for this project. My client has supplied graphics, page content and plenty of visuals so hopefully this will make things easier
Updates

To all designers,

Thanks all your designs. Just to let you all know they have been sent to the client and I will supply feedback to you all individually when I get it.

Many thanks,
Garth

Hi all,

We've had loads of designs for this project so thanks to you all very much. If there is any feedback to pass on, I will do this directly. Right now, all designs have been liked and are in the running. My client is going through them all and will make a decision on the deadline date which is the 10th May.
If you don't hear from me before then, it's simply because no alterations have been requested.

Many thanks.
Garth

Industry/Entity Type

Training

```html
<!DOCTYPE html>
<html lang="en">
<head>
<meta charset="utf-8">
<title>Keystone Consultancy Ltd. – What we Do</title>
<link rel="stylesheet" href="https://fonts.googleapis.com/css2?family=Montserrat:wght@400;500;600&family=Open+Sans:wght@400;600&family=Gochi+Hand&display=swap">
<style>
  :root {
    --page-green: #82c89a;
    --panel-yellow: #fff49c;
    --panel-edge: #e6d77a;
    --accent-orange: #f4511e;
    --heading-orange: #ef5a1c;
    --brand-blue: #1f6fd1;
    --footer-blue: #0b4ea9;
    --ink: #1e1e1e;
    --white: #ffffff;
    --frame-slate: #8fa3b5;
    --social-grey: #e4e4e4;
  }
  * { box-sizing: border-box; margin: 0; padding: 0; }
  html, body { width: 750px; height: 1200px; overflow: hidden; }
  body {
    position: relative;
    background: var(--page-green);
    font-family: "Montserrat", sans-serif;
    color: var(--ink);
  }
  .brand {
    position: absolute; left: 34px; top: 0; width: 82px; height: 118px;
    background: var(--white);
    box-shadow: 0 1px 3px rgba(0,0,0,.25);
  }
  .brand-art {
    position: absolute; left: 3px; top: 3px; width: 76px; height: 83px;
    background: linear-gradient(160deg, #cfe8f7, #7fbde8);
  }
  .brand-name {
    position: absolute; left: 0; right: 0; top: 92px;
    text-align: center; font-size: 8px; font-weight: 600; line-height: 1.3;
    color: var(--brand-blue);
  }
  .contact-card {
    position: absolute; left: 528px; top: 7px; width: 200px; height: 41px;
    background: var(--white);
    box-shadow: 2px 3px 5px rgba(0,0,0,.4);
    font-family: "Open Sans", sans-serif; font-size: 8.5px; line-height: 1.55;
    padding: 7px 0 0 9px;
  }
  .contact-card a { color: var(--brand-blue); text-decoration: none; }
  .main-nav { position: absolute; top: 79px; left: 0; }
  .main-nav a {
    position: absolute; top: 0; height: 24px;
    display: flex; align-items: center; justify-content: center; text-align: center;
    background: var(--accent-orange); color: var(--white);
    font-size: 11px; line-height: 1.05; text-decoration: none;
  }
  .intro-panel {
    position: absolute; left: 16px; top: 120px; width: 718px; height: 360px;
    background: var(--panel-yellow);
    border: 1px solid var(--panel-edge);
    box-shadow: 0 1px 3px rgba(0,0,0,.2);
  }
  .section-title {
    position: absolute; font-size: 14.5px; font-weight: 500; color: var(--heading-orange);
  }
  .section-body {
    position: absolute; font-size: 10.6px; line-height: 12.4px; white-space: nowrap;
  }
  .photo {
    position: absolute; padding: 11px; z-index: 2;
    box-shadow: 2px 3px 6px rgba(0,0,0,.35);
  }
  .photo span { display: block; width: 100%; height: 100%; }
  .photo-children {
    left: 458px; top: 198px; width: 255px; height: 184px;
    background: var(--frame-slate); transform: rotate(20deg);
  }
  .photo-children span { background: linear-gradient(135deg, #5d8a3c, #a9c777 55%, #d9c3a5); }
  .photo-play {
    left: 466px; top: 404px; width: 262px; height: 194px;
    background: var(--accent-orange); transform: rotate(-5deg); padding: 18px;
  }
  .photo-play span { background: linear-gradient(180deg, #8fb0c9, #6f6a5f 60%, #b7c36e); }
  .motto {
    position: absolute; left: 26px; top: 516px; white-space: nowrap;
    font-family: "Gochi Hand", cursive; font-size: 24px; letter-spacing: -0.5px; color: #111;
  }
  .site-footer {
    position: absolute; left: 16px; top: 604px; width: 718px; height: 192px; z-index: 1;
    background: var(--footer-blue); color: var(--white);
    box-shadow: 0 1px 3px rgba(0,0,0,.3);
  }
  .footer-title { position: absolute; top: 24px; font-size: 14px; font-weight: 500; text-align: center; }
  .quick-links { position: absolute; left: 26px; width: 160px; top: 56px; list-style: none; text-align: center; }
  .quick-links li { font-size: 14px; font-weight: 500; line-height: 16.4px; }
  .contact-line { position: absolute; left: 240px; display: flex; align-items: center; gap: 10px; font-size: 14px; font-weight: 500; }
  .social { position: absolute; left: 637px; width: 42px; height: 42px; border-radius: 50%; background: var(--social-grey); box-shadow: 0 1px 2px rgba(0,0,0,.3); }
</style>
</head>
<body>
  <div class="brand">
    <div class="brand-art" role="img" aria-label="Blue painted handprints artwork"></div>
    <p class="brand-name">Keystone<br>Consultancy Ltd.</p>
  </div>

  <div class="contact-card">
    <p>Email: <a href="#">enquiries@keystoneconsultancy.com</a></p>
    <p>Call: 07 700 900 418</p>
  </div>

  <nav class="main-nav">
    <a href="#" style="left:248px;width:74px">Home</a>
    <a href="#" style="left:330px;width:73px">Courses</a>
    <a href="#" style="left:410px;width:74px">PE Services</a>
    <a href="#" style="left:492px;width:73px">Consultant<br>Biopics</a>
    <a href="#" style="left:574px;width:73px">T &amp; L<br>Services</a>
    <a href="#" style="left:654px;width:73px">Resources</a>
  </nav>

  <section class="intro-panel">
    <h2 class="section-title" style="left:21px;top:14px">What we Do</h2>
    <p class="section-body" style="left:21px;top:44px">Keystone Consultancy specialises in providing bespoke Teaching and<br>Learning and Physical Education support to the primary education sector.<br>We offer a range of training and support methods, including team teaching,<br>INSET, courses, coaching, mentoring, staff meetings and so on.<br>Working with a diverse range of clients, such as individual primary and<br>secondary schools, clusters, Westmere County Council, School Sports Partnerships,<br>collaborations and Sports Coaches, we are committed to providing<br>professional development that has a real impact on school improvement.<br>Our consultants all bring with them a raft of experience in Primary Education,<br>Physical Education and School Improvement, plus the skills to inspire<br>and enthuse teachers.</p>
    <h2 class="section-title" style="left:19px;top:195px">Our Philosophy</h2>
    <p class="section-body" style="left:19px;top:225px">We are passionate about teaching and learning – both ours and yours!<br>We strive to practice what we preach and ensure that all our training<br>and support is personalised for the group or individual that it is created for.<br>We also know that our support is only as good as our own understanding,<br>so we are dedicated to ensuring our own professional development and<br>constantly reviewing and developing our practice.  We work in partnership<br>with our clients to design bespoke professional development opportunities,<br>constantly reviewing and developing the support with the client to ensure<br>their requirements are met.</p>
  </section>

  <div class="photo photo-children"><span role="img" aria-label="Photo of children exploring leaves outdoors"></span></div>
  <div class="photo photo-play"><span role="img" aria-label="Photo of children hanging upside down on a climbing frame"></span></div>

  <p class="motto">‘A teacher explains, a great teacher inspires’</p>

  <footer class="site-footer">
    <h3 class="footer-title" style="left:26px;width:160px">QUICK LINKS</h3>
    <ul class="quick-links">
      <li>Home</li><li>Courses</li><li>PE Services</li><li>Consultants Biopics</li><li>T &amp; L Services</li><li>Resourses</li>
    </ul>
    <h3 class="footer-title" style="left:320px;width:124px">CONTACTUS:</h3>
    <p class="contact-line" style="top:74px">
      <svg width="18" height="26" viewBox="0 0 18 26" aria-hidden="true"><rect x="1" y="1" width="16" height="24" rx="2" fill="none" stroke="#fff" stroke-width="2"/><rect x="4" y="4" width="10" height="7" fill="#fff"/><g fill="#fff"><rect x="4" y="14" width="2.5" height="2"/><rect x="8" y="14" width="2.5" height="2"/><rect x="12" y="14" width="2.5" height="2"/><rect x="4" y="18" width="2.5" height="2"/><rect x="8" y="18" width="2.5" height="2"/><rect x="12" y="18" width="2.5" height="2"/></g></svg>
      <span>07700900418</span>
    </p>
    <p class="contact-line" style="top:137px">
      <span style="font-size:24px;font-weight:600">@</span>
      <span>enquiries@keystoneconsultancy.com</span>
    </p>
    <span class="social" style="top:27px"></span>
    <span class="social" style="top:76px"></span>
    <span class="social" style="top:125px"></span>
  </footer>
</body>
</html>
```